Brightvale Circuit

Marion T Hadley
"Title" Adventure Manager & Host
2817 North 9th Street | Vancouver, BC | V5R 2K8
Direct 604.582. 1907 x 215
Chat drum41
1.800.436.5127
brightvale.ca
(perhaps small steady route bureau logo somewhere? Or “Powered by SRB”?)
- Grey/white logo cut out on reverse of card with web address

Industry/Entity Type

Travel

```html
<!DOCTYPE html>
<html lang="en">
<head>
<meta charset="utf-8">
<title>Brightvale Circuit – Business Card</title>
<link rel="stylesheet" href="https://fonts.googleapis.com/css2?family=Open+Sans:wght@400;600;700&display=swap">
<style>
  :root {
    --backdrop: #cccccc;
    --charcoal: #4a4a4a;
    --paper: #ffffff;
    --lime: #8cc63f;
    --ink: #555555;
    --rule: #111111;
  }
  * { margin: 0; padding: 0; box-sizing: border-box; }
  html, body {
    width: 1200px; height: 900px; overflow: hidden;
    background: var(--backdrop);
    font-family: "Open Sans", sans-serif;
  }
  .canvas { position: relative; width: 1200px; height: 900px; }
  .card {
    position: absolute; left: 274px; width: 655px; height: 373px;
    background: var(--charcoal); overflow: hidden;
  }
  .card--front { top: 70px; }
  .card--back { top: 459px; }
  .card__swoosh { position: absolute; inset: 0; width: 655px; height: 373px; }

  .holder-name {
    position: absolute; right: 26px; top: 24px;
    color: var(--paper); font-weight: 700; font-size: 23px;
  }
  .brand {
    position: absolute; display: flex; align-items: center; gap: 12px;
    font-weight: 600; font-size: 28px; letter-spacing: 0.5px;
  }
  .brand__mark { width: 22px; height: 22px; }
  .card--front .brand { left: 95px; top: 155px; color: var(--lime); }
  .card--front .brand__mark { background: var(--charcoal); }
  .card--back .brand { left: 0; right: 0; justify-content: center; top: 136px; color: var(--paper); }
  .card--back .brand__mark { background: var(--lime); }

  .contact {
    position: absolute; top: 273px; color: var(--ink);
    font-size: 14px; line-height: 20px;
  }
  .contact--title { left: 18px; }
  .contact--lines { left: 232px; }
  .contact--web { left: 443px; top: 297px; }
  .contact__divider {
    position: absolute; top: 265px; width: 4px; height: 73px; background: var(--rule);
  }
  .contact__divider--first { left: 212px; }
  .contact__divider--second { left: 427px; }
  .chat-dot {
    display: inline-block; width: 16px; height: 16px; border-radius: 50%;
    background: var(--charcoal); vertical-align: -3px; margin-right: 6px;
  }
  .back-rule {
    position: absolute; left: 33px; width: 588px; top: 310px;
    height: 3px; background: var(--paper);
  }
</style>
</head>
<body>
<div class="canvas">
  <section class="card card--front">
    <svg class="card__swoosh" viewBox="0 0 655 373" aria-hidden="true">
      <path d="M0,108 Q260,40 655,170" fill="none" stroke="#ffffff" stroke-width="4"/>
      <path d="M0,112 Q260,45 655,175 L655,248 Q330,40 0,117 Z" fill="#8cc63f"/>
      <path d="M0,117 Q330,40 655,248 L655,373 L0,373 Z" fill="#ffffff"/>
    </svg>
    <h1 class="holder-name">Marion T Hadley</h1>
    <div class="brand"><span class="brand__mark"></span>Brightvale Circuit</div>

    <p class="contact contact--title">Adventure Manager &amp; Host<br>2817 North 9th Street |<br>Vancouver, BC | V5R 2K8</p>
    <span class="contact__divider contact__divider--first"></span>
    <p class="contact contact--lines">Direct 604.582. 1907 x 215<br><span class="chat-dot"></span>Chat drum41<br>1.800.436.5127</p>
    <span class="contact__divider contact__divider--second"></span>
    <p class="contact contact--web">website: www.brightvale.ca</p>
  </section>

  <section class="card card--back">
    <div class="brand"><span class="brand__mark"></span>Brightvale Circuit</div>
    <span class="back-rule"></span>
  </section>
</div>
</body>
</html>
```